New Business Card Design Project

Looking for a modern business card design for an import distribution business for industrial technical products. The winning design will translate modern, sophistication, technical, professional and sustainable.

Target Market(s)

Technical customers

Industry/Entity Type

Business

Contact Information for Business Card

Dean Harlow
Sales Manager
M: 0471 625 183
P: 1300 872 619
dean@volkarsystems.com.au
4/18 Galloway Crest Road
Kestrel Vale NSW 2190
www.volkarsystems.com.au

Font styles to use
Sans Serif

Colors
ec1f27
606060
000000
fbfbfb

Requirements
Must have
• My Logo which is the Volkar Systems logo attached
Nice to have
• Eurostile Bold font

```html
<!DOCTYPE html>
<html lang="en">
<head>
<meta charset="utf-8">
<title>Volkar Systems – Business Card</title>
<link href="https://fonts.googleapis.com/css2?family=Poppins:wght@400;500&family=Saira:wdth,wght@112,800&display=swap" rel="stylesheet">
<style>
  :root {
    --red: #ec1f27;
    --deep-red: #5a0e0f;
    --grey: #606060;
    --dark-grey: #2b2d2f;
    --black: #000000;
    --white: #fbfbfb;
    --stage: #1d1e20;
  }
  * { margin: 0; padding: 0; box-sizing: border-box; }
  html, body {
    width: 1200px; height: 900px; overflow: hidden;
    background: var(--stage);
  }
  .canvas { position: relative; width: 1200px; height: 900px; }
  .card {
    position: absolute; left: 290px;
    width: 620px; height: 360px;
    border-radius: 22px; overflow: hidden;
    background: var(--black);
    box-shadow: 0 18px 40px rgba(0,0,0,.55);
  }
  .card--front { top: 50px; }
  .card--back { top: 490px; }
  .card__shapes { position: absolute; inset: 0; width: 100%; height: 100%; }

  /* front */
  .brand-lockup {
    position: absolute; left: 0; right: 0; top: 112px;
    display: flex; align-items: center; justify-content: center; gap: 18px;
  }
  .brand-lockup__square { width: 54px; height: 54px; background: var(--red); border-radius: 6px; }
  .brand-lockup__name {
    font-family: "Saira", sans-serif; font-weight: 800; font-stretch: 112%;
    font-size: 46px; letter-spacing: 2px; color: var(--red); text-transform: uppercase;
  }
  .web-band {
    position: absolute; left: 0; right: 0; top: 268px; height: 46px;
    background: var(--red);
    display: flex; align-items: center; justify-content: space-between;
    padding: 0 34px;
  }
  .web-band__url {
    font-family: "Poppins", sans-serif; font-weight: 500; font-size: 19px;
    letter-spacing: 1.4px; color: var(--white);
  }
  .web-band__arrow { width: 26px; height: 20px; }

  /* back */
  .person { position: absolute; left: 46px; top: 222px; }
  .person__name {
    font-family: "Saira", sans-serif; font-weight: 800; font-stretch: 112%;
    font-size: 34px; line-height: 1; color: var(--red); text-transform: uppercase;
  }
  .person__role {
    font-family: "Saira", sans-serif; font-weight: 800; font-stretch: 112%;
    font-size: 17px; letter-spacing: 1px; color: var(--grey); text-transform: uppercase; margin-top: 6px;
  }
  .contact {
    position: absolute; left: 338px; top: 40px; right: 28px;
    font-family: "Poppins", sans-serif; color: var(--white);
  }
  .contact__brand { display: flex; align-items: center; gap: 10px; margin-bottom: 16px; }
  .contact__brand-square { width: 28px; height: 28px; background: var(--red); border-radius: 4px; flex: none; }
  .contact__brand-name {
    font-family: "Saira", sans-serif; font-weight: 800; font-stretch: 112%;
    font-size: 22px; color: var(--red); text-transform: uppercase; letter-spacing: 1px; white-space: nowrap;
  }
  .contact__address { font-size: 14px; line-height: 1.45; margin-bottom: 10px; }
  .contact__list { list-style: none; font-size: 14px; line-height: 1.6; }
  .contact__list li { display: flex; align-items: center; gap: 10px; }
  .contact__icon { width: 14px; height: 14px; flex: none; }
</style>
</head>
<body>
<main class="canvas">

  <section class="card card--front" aria-label="Business card front">
    <svg class="card__shapes" viewBox="0 0 620 360" aria-hidden="true">
      <polygon points="0,60 120,0 620,300 620,360 560,360 0,50" fill="#140304"/>
      <polygon points="0,120 0,60 420,268 300,268" fill="#3a0708"/>
      <polygon points="330,0 410,0 200,360 120,360" fill="#111214"/>
      <polygon points="470,0 540,0 620,120 620,200" fill="#0e0f10"/>
    </svg>
    <div class="brand-lockup">
      <span class="brand-lockup__square"></span>
      <span class="brand-lockup__name">Volkar Systems</span>
    </div>
    <div class="web-band">
      <svg class="web-band__arrow" viewBox="0 0 26 20" aria-hidden="true"><path d="M2 10H22M14 3l8 7-8 7" fill="none" stroke="#fbfbfb" stroke-width="3.5"/></svg>
      <span class="web-band__url">www.volkarsystems.com.au</span>
      <svg class="web-band__arrow" viewBox="0 0 26 20" aria-hidden="true"><path d="M24 10H4M12 3l-8 7 8 7" fill="none" stroke="#fbfbfb" stroke-width="3.5"/></svg>
    </div>
  </section>

  <section class="card card--back" aria-label="Business card back">
    <svg class="card__shapes" viewBox="0 0 620 360" aria-hidden="true">
      <polygon points="250,0 330,0 250,170 160,170" fill="var(--dark-grey)"/>
      <polygon points="0,150 140,150 260,360 0,360" fill="var(--deep-red)"/>
      <polygon points="330,262 620,262 620,340 410,340" fill="var(--dark-grey)"/>
      <polygon points="140,150 250,180 260,360" fill="#0a0a0a"/>
    </svg>
    <div class="person">
      <p class="person__name">Dean Harlow</p>
      <p class="person__role">Sales Manager</p>
    </div>
    <div class="contact">
      <div class="contact__brand">
        <span class="contact__brand-square"></span>
        <span class="contact__brand-name">Volkar Systems</span>
      </div>
      <p class="contact__address">4/18 Galloway Crest Road<br>Kestrel Vale NSW 2190</p>
      <ul class="contact__list">
        <li><svg class="contact__icon" viewBox="0 0 14 14" aria-hidden="true"><rect x="3.5" y="1" width="7" height="12" rx="1.5" fill="none" stroke="#ec1f27" stroke-width="1.5"/><circle cx="7" cy="10.5" r=".9" fill="#ec1f27"/></svg>0471 625 183</li>
        <li><svg class="contact__icon" viewBox="0 0 14 14" aria-hidden="true"><path d="M1.5 5.5Q7 1 12.5 5.5L11 7 9 5.8V4.6Q7 4 5 4.6V5.8L3 7Z" fill="#ec1f27"/><rect x="3" y="8" width="8" height="5" rx="1" fill="none" stroke="#ec1f27" stroke-width="1.4"/></svg>1300 872 619</li>
        <li><svg class="contact__icon" viewBox="0 0 14 14" aria-hidden="true"><rect x="1" y="3" width="12" height="8.5" rx="1" fill="none" stroke="#ec1f27" stroke-width="1.4"/><path d="M1.5 3.6 7 8l5.5-4.4" fill="none" stroke="#ec1f27" stroke-width="1.4"/></svg>dean@volkarsystems.com.au</li>
        <li><svg class="contact__icon" viewBox="0 0 14 14" aria-hidden="true"><circle cx="7" cy="7" r="5.8" fill="none" stroke="#ec1f27" stroke-width="1.4"/><ellipse cx="7" cy="7" rx="2.4" ry="5.8" fill="none" stroke="#ec1f27" stroke-width="1.2"/><path d="M1.2 7h11.6" stroke="#ec1f27" stroke-width="1.2"/></svg>www.volkarsystems.com.au</li>
      </ul>
    </div>
  </section>

</main>
</body>
</html>
```